Whimsical Flyer for Children's Storytime at Glow And Grow

Design an 8 1/2 by 11 color flyer to promote a storytime series at our store. At Glow And Grow we believe that the shortest distance between two people is a story. Everything in our store has a story behind it and now we are excited to have one of the world’s best storytellers coming to share her gifts with kids ages 2-5, once a week, starting at 10am on July 7th for an eight-week series. Ms. Dolores (Pemberley), children’s librarian and storyteller extraordinaire, and our own Mr. Toby, her budding apprentice, will regale children with music, stories and movement, FREE! 10am. Reservations required. Visit glowandgrow.example for details. 872 E. 61st Street - San Mateo CA 94417.

Target Market(s)

Parents and caregivers with children

Requirements
Must have
• Whimsy, fun, enticing to parents and children

```html
<!DOCTYPE html>
<html lang="en">
<head>
<meta charset="utf-8">
<title>Storytime at Glow And Grow</title>
<link href="https://fonts.googleapis.com/css2?family=Fredoka:wght@500;700&family=Open+Sans:wght@400;600;700&display=swap" rel="stylesheet">
<style>
  :root {
    --green: #5fae2a;
    --magenta: #d62a80;
    --magenta-soft: #e95aa0;
    --orange: #f07b22;
    --olive: #8a8d2a;
    --ink: #2f2f2f;
    --paper: #ffffff;
    --sky: #6ac3e8;
    --sun: #f6c63a;
  }
  * { box-sizing: border-box; margin: 0; padding: 0; }
  html, body { width: 876px; height: 1200px; overflow: hidden; background: var(--paper); }
  .flyer { position: relative; width: 876px; height: 1200px; background: var(--paper); font-family: "Open Sans", sans-serif; color: var(--ink); overflow: hidden; }
  .swooshes { position: absolute; inset: 0; }
  .hero-photo { position: absolute; left: 190px; top: 60px; width: 470px; height: 480px; border-radius: 6px;
    background: linear-gradient(160deg, #d9d2c8 0%, #b7a48f 45%, #3a3a3a 100%); }
  .kids-art { position: absolute; left: 28px; top: 50px; width: 170px; height: 170px; border-radius: 50%;
    background: radial-gradient(circle at 45% 40%, #ffd36a, #6fbf3f 70%); }
  .mascot-art { position: absolute; left: 48px; top: 600px; width: 150px; height: 190px; border-radius: 24px;
    background: linear-gradient(180deg, #f7c33c, #e8872a); }
  .headline { position: absolute; left: 200px; width: 640px; top: 590px; text-align: center;
    font-family: "Fredoka", sans-serif; font-weight: 700; color: var(--green); line-height: 1; }
  .headline .line1 { font-size: 62px; }
  .headline .line2 { font-size: 74px; }
  .storyteller { position: absolute; left: 200px; width: 640px; top: 740px; text-align: center;
    font-family: "Fredoka", sans-serif; font-weight: 700; font-size: 38px; color: var(--magenta); white-space: nowrap; }
  .date-band { position: absolute; left: 0; right: 0; top: 796px; height: 96px; background: var(--magenta); color: var(--paper); text-align: center; }
  .date-band .start { font-family: "Fredoka", sans-serif; font-weight: 700; font-size: 44px; line-height: 58px; padding-top: 2px; }
  .date-band .series { font-family: "Fredoka", sans-serif; font-weight: 500; font-size: 24px; line-height: 30px; }
  .intro { position: absolute; left: 40px; right: 40px; top: 904px; text-align: center; font-size: 16px; line-height: 1.4; }
  .intro strong { font-weight: 700; }
  .brand { position: absolute; left: 50px; top: 1018px; display: flex; align-items: center; gap: 10px; white-space: nowrap; }
  .brand-dot { width: 44px; height: 44px; border-radius: 50%; background: var(--orange); flex: none; }
  .brand-name { font-family: "Fredoka", sans-serif; font-weight: 700; font-size: 28px; color: var(--olive); }
  .reserve { position: absolute; right: 40px; top: 982px; width: 420px; text-align: center; }
  .reserve .label { font-family: "Fredoka", sans-serif; font-weight: 700; font-size: 22px; line-height: 28px; color: var(--orange); }
  .reserve .visit { margin-top: 4px; border: 3px solid var(--magenta); border-radius: 6px; padding: 3px 10px; white-space: nowrap;
    font-family: "Fredoka", sans-serif; font-weight: 700; font-size: 29px; color: var(--magenta); }
  .reserve .address { margin-top: 8px; font-size: 14px; white-space: nowrap; }
  .motto-band { position: absolute; left: 0; right: 0; bottom: 0; height: 70px; background: var(--orange); color: var(--paper); white-space: nowrap;
    display: flex; align-items: center; justify-content: center; font-family: "Fredoka", sans-serif; font-weight: 700; font-size: 22px; letter-spacing: 0.5px; }
</style>
</head>
<body>
<main class="flyer">
  <svg class="swooshes" width="876" height="1200" viewBox="0 0 876 1200" aria-hidden="true">
    <path d="M0 360 C200 300 420 420 876 250 L876 330 C460 480 220 380 0 430 Z" fill="var(--sky)" opacity="0.35"/>
    <path d="M0 440 C260 380 520 520 876 380 L876 430 C520 570 260 450 0 500 Z" fill="var(--green)" opacity="0.35"/>
    <path d="M0 500 C300 470 560 560 876 470 L876 500 C560 600 300 520 0 545 Z" fill="var(--magenta-soft)" opacity="0.4"/>
    <path d="M560 0 C640 120 760 160 876 150 L876 0 Z" fill="var(--sun)" opacity="0.35"/>
    <circle cx="790" cy="430" r="30" fill="none" stroke="var(--orange)" stroke-width="8"/>
    <circle cx="720" cy="540" r="18" fill="none" stroke="var(--sky)" stroke-width="6"/>
    <circle cx="820" cy="560" r="22" fill="none" stroke="#2d4fa3" stroke-width="6"/>
    <circle cx="120" cy="470" r="20" fill="none" stroke="var(--green)" stroke-width="6"/>
  </svg>

  <div class="kids-art" role="img" aria-label="Illustration of two children riding on an open book"></div>
  <div class="hero-photo" role="img" aria-label="Photo of the storyteller holding a picture book beside a Welcome to Storytime board"></div>
  <div class="mascot-art" role="img" aria-label="Cartoon book character with a pencil"></div>

  <h1 class="headline"><span class="line1">WORLD'S BEST</span><br><span class="line2">STORYTELLERS</span></h1>
  <p class="storyteller">MS. DOLORES (PEMBERLEY)</p>

  <section class="date-band">
    <p class="start">STARTING AT 10AM ON JULY 7TH</p>
    <p class="series">KIDS AGES 2-5 &nbsp;|&nbsp; 8 WEEK SERIES</p>
  </section>

  <p class="intro">Children's librarian and storyteller extraordinaire, and our own <strong>Mr. Toby</strong>, her budding apprentice, will regale children with music, stories and movement, <strong>FREE! 10am.</strong></p>

  <div class="brand">
    <span class="brand-dot"></span>
    <span class="brand-name">Glow And Grow</span>
  </div>

  <div class="reserve">
    <p class="label">RESERVATIONS REQUIRED.</p>
    <p class="visit">Visit glowandgrow.example</p>
    <p class="address">For details · 872 E. 61st Street - San Mateo CA 94417</p>
  </div>

  <footer class="motto-band">WE BELIEVE THAT THE SHORTEST DISTANCE BETWEEN TWO PEOPLE IS A STORY</footer>
</main>
</body>
</html>
```